Moxtrel Compensation Lawyers

We need a modern, sleek letterhead that is professional.

In relation to the footer, we would like to have firm contact details there ideally, however you must also insert at the bottom of each page the following....

Liability limited by a scheme approved under the Professional Standards Legislation.

From the attachment you can extract the firm logo. Also, I would like the Accredited specialist circle on the letterhead also.

Also, I would like you to create a document that can easily be edited for change of contact details, as these are likely to change.

Industry/Entity Type

It Professional

Font styles to use
Sans Serif

Colors
0655a3
3276b5
85abd2
0492cd
33a6d7
85cae6
cee9f5
eaf1f7
cbcbcb

Requirements
Must have
• Ph: 9317-2856
• F: 9184-3720
• M 0435-618-294
• kp@moxtrel.com.au
• www.moxtrel.com.au
Nice to have
• the word document gives you an idea of what I like. I am happy for your to amaze me with your creativity.

```html
<!DOCTYPE html>
<html lang="en">
<head>
<meta charset="utf-8">
<title>Moxtrel Compensation Lawyers – Letterhead</title>
<link rel="stylesheet" href="https://fonts.googleapis.com/css2?family=Open+Sans:wght@400;600&display=swap">
<style>
  :root {
    --navy: #0655a3;
    --blue: #3276b5;
    --sky: #85abd2;
    --cyan: #0492cd;
    --cyan-mid: #33a6d7;
    --cyan-soft: #85cae6;
    --cyan-pale: #cee9f5;
    --mist: #eaf1f7;
    --grey: #cbcbcb;
    --ink: #1f2a33;
    --footer-band: #0a93cf;
    --footer-strip: #1aa9e4;
    --backdrop: #eef2f5;
    --paper: #ffffff;
  }
  html, body {
    margin: 0;
    width: 1200px;
    height: 900px;
    overflow: hidden;
    background: var(--backdrop);
    font-family: "Open Sans", Arial, sans-serif;
  }
  .letterhead {
    position: absolute;
    left: 300px;
    top: 26px;
    width: 600px;
    height: 848px;
    background: var(--paper);
    box-shadow: 0 4px 18px rgba(0, 0, 0, 0.14);
    overflow: hidden;
  }
  .corner-art {
    position: absolute;
  }
  .corner-art--left {
    left: 0;
    top: 0;
    width: 230px;
    height: 190px;
    background: linear-gradient(135deg, var(--navy) 0%, var(--cyan) 45%, var(--cyan-soft) 100%);
    clip-path: polygon(0 0, 100% 0, 0 100%);
  }
  .corner-art--right {
    right: 0;
    top: 50px;
    width: 60px;
    height: 150px;
    background: linear-gradient(180deg, var(--cyan-soft) 0%, var(--cyan) 100%);
    clip-path: polygon(100% 0, 100% 100%, 0 65%);
  }
  .header-rule {
    position: absolute;
    left: 60px;
    top: 110px;
    width: 488px;
    height: 1px;
    background: var(--cyan-mid);
    transform-origin: 0 0;
    transform: rotate(4.3deg);
  }
  .brand {
    position: absolute;
    right: 52px;
    top: 58px;
    display: flex;
    flex-direction: column;
    align-items: center;
    gap: 8px;
  }
  .brand__dot {
    width: 26px;
    height: 26px;
    border-radius: 50%;
    background: var(--cyan-mid);
  }
  .brand__name {
    font-size: 18px;
    font-weight: 400;
    color: var(--ink);
    white-space: nowrap;
  }
  .footer-band {
    position: absolute;
    left: 0;
    right: 0;
    bottom: 0;
    height: 100px;
    background: var(--footer-band);
  }
  .footer-strip {
    position: absolute;
    left: 0;
    right: 0;
    bottom: 0;
    height: 24px;
    background: var(--footer-strip);
  }
  .contacts {
    position: absolute;
    left: 56px;
    right: 44px;
    bottom: 40px;
    display: flex;
    justify-content: space-between;
    margin: 0;
    padding: 0;
    list-style: none;
  }
  .contacts__item {
    display: flex;
    align-items: center;
    gap: 5px;
    font-size: 8px;
    color: #ffffff;
    white-space: nowrap;
  }
  .contacts__icon {
    width: 12px;
    height: 12px;
    fill: #ffffff;
  }
  .legal-note {
    position: absolute;
    left: 0;
    right: 0;
    bottom: 7px;
    margin: 0;
    text-align: center;
    font-size: 7.5px;
    color: #0b2a3f;
  }
</style>
</head>
<body>
  <main class="letterhead">
    <div class="corner-art corner-art--left" role="img" aria-label="Angular blue corner decoration"></div>
    <div class="corner-art corner-art--right" role="img" aria-label="Angular blue edge decoration"></div>
    <div class="header-rule"></div>

    <header class="brand">
      <span class="brand__dot"></span>
      <span class="brand__name">Moxtrel &amp; Co</span>
    </header>

    <footer>
      <div class="footer-band"></div>
      <div class="footer-strip"></div>
      <ul class="contacts">
        <li class="contacts__item">
          <svg class="contacts__icon" viewBox="0 0 24 24"><path d="M6.6 10.8a15.1 15.1 0 0 0 6.6 6.6l2.2-2.2a1 1 0 0 1 1-.25 11.4 11.4 0 0 0 3.6.57 1 1 0 0 1 1 1V20a1 1 0 0 1-1 1A17 17 0 0 1 3 4a1 1 0 0 1 1-1h3.5a1 1 0 0 1 1 1c0 1.25.2 2.45.57 3.57a1 1 0 0 1-.25 1z"/></svg>
          9317-2856
        </li>
        <li class="contacts__item">
          <svg class="contacts__icon" viewBox="0 0 24 24"><path d="M7 1h10a2 2 0 0 1 2 2v18a2 2 0 0 1-2 2H7a2 2 0 0 1-2-2V3a2 2 0 0 1 2-2zm0 3v15h10V4zm5 16.2a1 1 0 1 0 0 2 1 1 0 0 0 0-2z"/></svg>
          0435-618-294
        </li>
        <li class="contacts__item">
          <svg class="contacts__icon" viewBox="0 0 24 24"><path d="M7 2h10v5H7zM4 8h16a2 2 0 0 1 2 2v7h-4v5H6v-5H2v-7a2 2 0 0 1 2-2zm4 8v4h8v-4z"/></svg>
          9184-3720
        </li>
        <li class="contacts__item">
          <svg class="contacts__icon" viewBox="0 0 24 24"><path d="M2 5h20v14H2zm2 2v.5l8 5 8-5V7zm0 2.8V17h16V9.8l-8 5z"/></svg>
          kp@moxtrel.com.au
        </li>
        <li class="contacts__item">
          <svg class="contacts__icon" viewBox="0 0 24 24"><path d="M12 2a10 10 0 1 0 0 20 10 10 0 0 0 0-20zm0 2c.8 1.1 1.5 2.5 1.9 4h-3.8c.4-1.5 1.1-2.9 1.9-4zM4.3 14a8 8 0 0 1 0-4h3.4a16 16 0 0 0 0 4zm5.4 0a14 14 0 0 1 0-4h4.6a14 14 0 0 1 0 4zm6.6 0a16 16 0 0 0 0-4h3.4a8 8 0 0 1 0 4zM12 20c-.8-1.1-1.5-2.5-1.9-4h3.8c-.4 1.5-1.1 2.9-1.9 4z"/></svg>
          www.moxtrel.com.au
        </li>
      </ul>
      <p class="legal-note">Liability limited by a scheme approved under the Professional Standards Legislation.</p>
    </footer>
  </main>
</body>
</html>
```